Branvique needs a business Card Design

We are looking for a business card Design for our new Managed Service Provider Company, Branvique. Branvique encompasses everything IT for the average medium sized business. Our primary services are help desk support, cyber-security (malware and ransomware protection), and Disaster Recovery systems. We would like the design to have a very clean and professional look, with a very minimalist feel.

Target Market(s)

Medium to large sized businesses

Industry/Entity Type

It Service

Contact Information for Business Card

Name GoesHere
name@branvique.com
O: 555-382-6047
C: 555-731-5820

Font styles to use
Other font styles liked:
• Poppins Font Only Please

Colors

Designer to choose only greyscale colors for use in the design.

Requirements
Must have
• Logo included
Nice to have
• Cutting Edge, innovative, minimalistic, elegant

```html
<!DOCTYPE html>
<html lang="en">
<head>
<meta charset="utf-8">
<title>Branvique Business Card</title>
<link rel="stylesheet" href="https://fonts.googleapis.com/css2?family=Poppins:wght@400;500;700&display=swap">
<style>
  :root {
    --navy: #0b2540;
    --paper: #f4f4f4;
    --paper-shade: #e6e6e6;
    --ink: #0b2540;
    --stage: #d9d9d9;
    --card-shadow: rgba(0, 0, 0, 0.28);
  }
  * { margin: 0; padding: 0; box-sizing: border-box; }
  html, body {
    width: 1200px;
    height: 1021px;
    overflow: hidden;
    background: var(--stage);
    font-family: "Poppins", sans-serif;
  }
  .stage { position: relative; width: 1200px; height: 1021px; }

  .card {
    position: absolute;
    width: 640px;
    height: 366px;
    box-shadow: 0 14px 30px var(--card-shadow);
  }

  /* Front */
  .card-front {
    left: 430px;
    top: 120px;
    background: var(--navy);
    display: flex;
    align-items: center;
    justify-content: center;
  }
  .wordmark {
    font-weight: 400;
    text-transform: uppercase;
    letter-spacing: 0.42em;
    font-size: 26px;
    line-height: 1;
  }
  .card-front .wordmark { color: #ffffff; margin-right: -0.42em; }

  /* Back */
  .card-back {
    left: 130px;
    top: 460px;
    background: linear-gradient(100deg, var(--paper-shade) 0%, var(--paper) 45%, #fafafa 100%);
    color: var(--ink);
  }
  .card-back .wordmark {
    position: absolute;
    left: 44px;
    top: 78px;
    color: var(--ink);
  }
  .contact-list {
    position: absolute;
    left: 44px;
    top: 214px;
    list-style: none;
    font-size: 17px;
    line-height: 26px;
    font-weight: 400;
  }
  .contact-list li { display: flex; align-items: center; gap: 8px; }
  .contact-list svg { width: 15px; height: 15px; flex: none; }

  .person {
    position: absolute;
    right: 44px;
    top: 236px;
    text-align: right;
  }
  .person-name { font-weight: 700; font-size: 22px; line-height: 1.2; }
  .person-title { font-weight: 400; font-size: 17px; line-height: 1.3; }

  .edge-tab {
    position: absolute;
    right: 0;
    top: 244px;
    width: 14px;
    height: 44px;
    background: var(--navy);
    border-radius: 6px 0 0 6px;
  }
</style>
</head>
<body>
<main class="stage">
  <section class="card card-front" aria-label="Card front">
    <p class="wordmark">Branvique</p>
  </section>

  <section class="card card-back" aria-label="Card back">
    <p class="wordmark">Branvique</p>

    <ul class="contact-list">
      <li>
        <svg viewBox="0 0 24 24" aria-hidden="true"><path fill="currentColor" d="M6.6 10.8a15.1 15.1 0 0 0 6.6 6.6l2.2-2.2a1 1 0 0 1 1-.25 11.4 11.4 0 0 0 3.6.57 1 1 0 0 1 1 1V20a1 1 0 0 1-1 1A17 17 0 0 1 3 4a1 1 0 0 1 1-1h3.5a1 1 0 0 1 1 1c0 1.25.2 2.45.57 3.6a1 1 0 0 1-.25 1z"/></svg>
        <span>555-382-6047</span>
      </li>
      <li>
        <svg viewBox="0 0 24 24" aria-hidden="true"><rect x="6" y="2" width="12" height="20" rx="2" fill="none" stroke="currentColor" stroke-width="2"/><circle cx="12" cy="18" r="1.2" fill="currentColor"/></svg>
        <span>555-731-5820</span>
      </li>
      <li>
        <svg viewBox="0 0 24 24" aria-hidden="true"><rect x="2" y="5" width="20" height="14" rx="1" fill="none" stroke="currentColor" stroke-width="2"/><path d="M2 6l10 7 10-7M2 18l7-6M22 18l-7-6" fill="none" stroke="currentColor" stroke-width="2"/></svg>
        <span>name@branvique.com</span>
      </li>
      <li>
        <svg viewBox="0 0 24 24" aria-hidden="true"><circle cx="12" cy="12" r="9.5" fill="none" stroke="currentColor" stroke-width="2"/><ellipse cx="12" cy="12" rx="4" ry="9.5" fill="none" stroke="currentColor" stroke-width="1.6"/><path d="M2.5 12h19M4 7h16M4 17h16" stroke="currentColor" stroke-width="1.6"/></svg>
        <span>www.branvique.com</span>
      </li>
    </ul>

    <div class="person">
      <p class="person-name">Daniel Harper</p>
      <p class="person-title">Founder</p>
    </div>

    <div class="edge-tab" aria-hidden="true"></div>
  </section>
</main>
</body>
</html>
```